'Ormel Property Development' Business Card

Business Card Features:

High Quality (potentially textured) thick card - preference is white textured card

Logo (supplied)

We plan to use the vertical logo as the main logo. But i am happy for people to use either if they find it works better for the design of the card.

The building icon and also the insert to the 'E' is in a metallic finish, i think this should be finished in a metallic embossed or raised style.
Updates

Please note i have attached both a horizontal and Vertical Logo for your reference. We plan to use the vertical logo as the main logo. But i am happy for people to use either if they find it works better for the design of the card.

Please note i am considering having the cards made on stainless steel. This introduces the option of having cut outs in the card and etching or printing for the design. If you have a good concept for this please submit.

http://www.tinquarry.example/black-metal-cards# this is a site that makes the metal cards to offer some direction . . . . Please note i am basic the selection o the best design, if that means normal print cards on paper then this is what i will choose. But there are some great options with the metal. Thanks.

Industry/Entity Type

Building

Requirements
Must have
• Helvetica font to details side of card - logo as supplied to opposite side.

Card Details:

Darrow Pketts
Managing Director

+61 487 263 518
+61 3 6172 4809

PO Box 73
Bentleigh, VIC 3024

darrow@ormel.example

www.ormel.example

```html
<!DOCTYPE html>
<html lang="en">
<head>
<meta charset="utf-8">
<title>Ormel Property Development – Business Card</title>
<link href="https://fonts.googleapis.com/css2?family=Arimo:wght@400;700&display=swap" rel="stylesheet">
<style>
  :root {
    --page: #2b2b2b;
    --steel-light: #e9e9e9;
    --steel-mid: #c9c9c9;
    --steel-dark: #a9a9a9;
    --etch: #4a4a4a;
    --etch-soft: #5c5c5c;
    --edge: #8e8e8e;
  }
  * { margin: 0; padding: 0; box-sizing: border-box; }
  html, body {
    width: 1200px;
    height: 849px;
    overflow: hidden;
    background: var(--page);
  }
  .canvas {
    position: relative;
    width: 1200px;
    height: 849px;
    background: var(--page);
  }
  .card {
    position: absolute;
    left: 110px;
    top: 120px;
    width: 980px;
    height: 609px;
    border-radius: 26px;
    border: 1px solid var(--edge);
    background:
      repeating-linear-gradient(180deg, rgba(255,255,255,0.18) 0 1px, rgba(0,0,0,0.04) 1px 3px),
      linear-gradient(100deg, var(--steel-dark) 0%, var(--steel-light) 38%, var(--steel-mid) 62%, var(--steel-light) 82%, var(--steel-dark) 100%);
    font-family: "Arimo", "Helvetica Neue", Helvetica, Arial, sans-serif;
    color: var(--etch);
  }
  .brand {
    position: absolute;
    left: 120px;
    top: 230px;
    display: flex;
    align-items: center;
    gap: 22px;
  }
  .brand-mark {
    width: 56px;
    height: 56px;
    background: var(--etch);
    flex: none;
  }
  .brand-name {
    font-size: 30px;
    font-weight: 700;
    line-height: 1.2;
    color: var(--etch);
    width: 290px;
  }
  .details {
    position: absolute;
    left: 560px;
    top: 64px;
  }
  .person-name {
    font-size: 34px;
    font-weight: 400;
    color: var(--etch-soft);
  }
  .person-role {
    font-size: 22px;
    text-transform: uppercase;
    color: var(--etch-soft);
    margin-top: 4px;
  }
  .contact-list {
    list-style: none;
    margin-top: 76px;
  }
  .contact-list li {
    display: flex;
    align-items: center;
    gap: 16px;
    font-size: 25px;
    line-height: 36px;
    color: var(--etch);
  }
  .contact-list li.address {
    align-items: flex-start;
    margin-top: 30px;
    line-height: 34px;
  }
  .contact-list li.web { margin-top: 26px; gap: 22px; }
  .icon { width: 20px; height: 20px; flex: none; }
  .address .icon { margin-top: 7px; }
</style>
</head>
<body>
<main class="canvas">
  <section class="card" aria-label="Business card, details side">
    <div class="brand">
      <span class="brand-mark" aria-hidden="true"></span>
      <span class="brand-name">Ormel Property Development</span>
    </div>

    <div class="details">
      <p class="person-name">Darrow Pketts</p>
      <p class="person-role">Managing Director</p>

      <ul class="contact-list">
        <li>
          <svg class="icon" viewBox="0 0 20 20" aria-hidden="true"><path d="M5 2 L8 6 L6 8 Q8 12 12 14 L14 12 L18 15 L16 18 Q8 18 2 6 Z" fill="none" stroke="#4a4a4a" stroke-width="1.6"/></svg>
          0487263518
        </li>
        <li>
          <svg class="icon" viewBox="0 0 20 20" aria-hidden="true"><rect x="5" y="2" width="10" height="16" rx="1.5" fill="none" stroke="#4a4a4a" stroke-width="1.6"/><line x1="8" y1="15" x2="12" y2="15" stroke="#4a4a4a" stroke-width="1.6"/></svg>
          1800 613 472
        </li>
        <li>
          <svg class="icon" viewBox="0 0 20 20" aria-hidden="true"><rect x="2" y="5" width="16" height="11" fill="none" stroke="#4a4a4a" stroke-width="1.6"/><path d="M2 5 L10 11 L18 5" fill="none" stroke="#4a4a4a" stroke-width="1.6"/></svg>
          darrow@ormel.example
        </li>
        <li class="address">
          <svg class="icon" viewBox="0 0 20 20" aria-hidden="true"><path d="M10 19 Q3 11 3 8 A7 7 0 0 1 17 8 Q17 11 10 19 Z" fill="none" stroke="#4a4a4a" stroke-width="1.6"/><circle cx="10" cy="8" r="2.4" fill="#4a4a4a"/></svg>
          <span>PO BOX 73 BENTLEIGH,<br>VIC 3024</span>
        </li>
        <li class="web">
          <svg class="icon" viewBox="0 0 20 20" aria-hidden="true"><circle cx="10" cy="10" r="8" fill="none" stroke="#4a4a4a" stroke-width="1.6"/><ellipse cx="10" cy="10" rx="3.5" ry="8" fill="none" stroke="#4a4a4a" stroke-width="1.3"/><line x1="2" y1="10" x2="18" y2="10" stroke="#4a4a4a" stroke-width="1.3"/></svg>
          www.ormel.example
        </li>
      </ul>
    </div>
  </section>
</main>
</body>
</html>
```